Anatomic 3D models + Urological Robotic surgery site

I want a website to represent my business as a developer of 3D models (reconstructions based on CT and MRI scans) and urological robotic surgery. The main point I need on my website is that it is modern, very attractive, clean, responsive and an interaction that differentiate me from the usual websites they have in my market. The site will be in portuguese and I'll provide the content to be used. The company name would be my name: Dr Mateus Vilhena. The colors and other choices I made here are not final decisions. If you have a suggestion you, they are welcome.

Target Market(s)

My patients

Industry/Entity Type

Medical

Coding

Number of Pages Required

1 page

Font styles to use
Sans Serif

Colors
0054AA
0677BA
7BADD7
CADEEF
E8F1F8
0094D4
00A9DD
6FCCEA
C7EBF8
E9F6FB
00AB8E
00BBA5
67D7C9
C6EFE9
E9F9F6
59FF00
82FF00
B8FF75
E3FFCB
F4FFEA
FFC000
F8CF3A
FAE287
FDF2CF
FEFAEE
F0912C
F2A743
F7CA91
FBE8D2
FDF5EE
A7469A
B969AE
D3A5CF
EDDBEB
F8F0F9
6B429C
8869AF
B7A5CE
E3DAEB
F3F0F8

Requirements
Must have
• Responsive, clean, modern, attractive, stand out from usual sites.
Should not have
• Antiquate boring designs.

```html
<!DOCTYPE html>
<html lang="en">
<head>
<meta charset="utf-8">
<title>Dr. Mateus Vilhena – Urological Robotic Surgery</title>
<link rel="stylesheet" href="https://fonts.googleapis.com/css2?family=Sora:wght@300;400;500&family=Poppins:wght@400;500;600&display=swap">
<style>
:root{
  --teal:#2f7192;
  --teal-light:#4a8aa9;
  --green:#8cc63f;
  --green-light:#a6d468;
  --ink:#1f1f1f;
  --text:#4a4a4a;
  --muted-bg:#ececec;
  --line:#d6d6d6;
  --footer:#222222;
  --white:#ffffff;
}
*{margin:0;padding:0;box-sizing:border-box}
html,body{width:1200px;height:5240px;overflow:hidden}
body{font-family:"Poppins",sans-serif;color:var(--text);background:var(--white);position:relative;font-size:13px;line-height:1.45}
h1,h2,.brand{font-family:"Sora",sans-serif;font-weight:400;color:var(--ink);letter-spacing:-0.5px}
.accent{color:var(--green)}
section{position:relative;width:1200px}
.abs{position:absolute}
b{color:var(--ink);font-weight:600}

/* hero */
.hero{height:702px;background:linear-gradient(100deg,#e6e6e6 0%,#d9d9d9 45%,#bcc2c6 70%,#9fb0bd 100%)}
.hero-photo{left:560px;top:0;width:640px;height:702px;background:radial-gradient(circle at 55% 45%,#c9d3da 0%,#aebbc6 40%,#8fa3b2 70%,transparent 100%)}
.nav{left:88px;top:32px;width:1024px;height:70px;background:var(--white);border-radius:10px;display:flex;align-items:center;padding:0 26px;box-shadow:0 4px 14px rgba(0,0,0,.06)}
.nav .brand{font-size:20px;color:var(--ink)}
.nav ul{list-style:none;display:flex;gap:26px;margin-left:auto;font-size:11px;text-transform:uppercase;color:var(--ink);font-weight:500}
.nav .lang{margin-left:30px;padding-left:24px;border-left:1px solid var(--line);font-size:11px;font-weight:600;color:var(--ink)}
.hero h1{left:88px;top:236px;font-size:60px;line-height:63px;width:560px}
.hero p{left:88px;top:454px;width:450px;font-size:13px;color:#333}
.dots{left:88px;top:632px;display:flex;gap:10px}
.dots span{width:30px;height:4px;border-radius:2px;background:#a9a9a9}
.dots span:first-child{background:var(--green)}

/* intro */
.intro{height:687px}
.intro-text{left:148px;top:125px;width:456px;font-size:12.5px;line-height:18px}
.intro-text p{margin-bottom:18px}
.offer-box{left:647px;top:87px;width:362px;height:438px;background:var(--teal);border-radius:24px;padding:52px 40px 0 42px;color:var(--white)}
.offer{display:flex;align-items:center;gap:22px;margin-bottom:40px;font-size:12px;line-height:17px}
.offer .num{flex:none;width:64px;height:64px;border-radius:50%;background:var(--green);display:flex;align-items:center;justify-content:center;font-family:"Sora",sans-serif;font-size:28px;font-weight:500}
.goal{left:0;top:592px;width:1200px;text-align:center;font-size:12.5px}
.divider{left:88px;top:686px;width:1024px;height:1px;background:var(--line)}

/* about */
.about{height:574px}
.about .back-square{left:134px;top:88px;width:132px;height:132px;background:#d4e3ea;border-radius:14px}
.about .frame{left:380px;top:250px;width:238px;height:233px;border-right:3px dashed var(--green);border-bottom:3px dashed var(--green);border-radius:0 0 22px 0}
.about .photo{left:175px;top:128px;width:417px;height:330px;border-radius:20px;background:linear-gradient(135deg,#8c8c8c,#5f6f78 50%,#3f6f8c);}
.about h2{left:671px;top:178px;font-size:34px}
.about .copy{left:671px;top:238px;width:400px;font-size:12.5px;line-height:18px}
.about .copy p{margin-bottom:14px}

/* approach */
.approach{height:604px;background:var(--muted-bg);overflow:hidden}
.approach h2{left:88px;top:96px;font-size:34px}
.approach .copy{left:88px;top:150px;width:440px;font-size:12.5px;line-height:18px}
.approach .copy p{margin-bottom:14px}
.checks{list-style:none;width:440px}
.checks li{display:flex;gap:12px;padding:10px 0;border-bottom:1px solid var(--line);font-size:12.5px;line-height:18px}
.checks li:last-child{border-bottom:none}
.checks svg{flex:none;margin-top:2px}
.approach .circle{left:670px;top:48px;width:410px;height:410px;border-radius:50%;background:var(--white)}
.approach .robot{left:570px;top:0;width:630px;height:480px;background:radial-gradient(ellipse at 60% 40%,rgba(190,196,200,.75) 0%,rgba(200,205,208,.35) 45%,transparent 70%)}
.approach .focus{left:0;top:510px;width:1200px;text-align:center;font-size:12.5px;line-height:22px}

/* planning */
.planning{height:993px}
.planning .frame{left:128px;top:258px;width:232px;height:209px;border-left:3px dashed var(--green);border-bottom:3px dashed var(--green);border-radius:0 0 0 22px}
.planning .media{left:159px;top:93px;width:504px;height:363px;border-radius:20px;background:linear-gradient(160deg,#8ea0d8 0%,#a8b0e2 40%,#c9bf96 60%,#9aa8dc 100%)}
.play{left:527px;top:408px;width:90px;height:90px;border-radius:50%;background:var(--teal);display:flex;align-items:center;justify-content:center}
.planning-title{left:712px;top:148px;font-size:34px;line-height:44px;width:340px}
.planning .copy{left:712px;top:248px;width:380px;font-size:12.5px;line-height:18px}
.support-head{left:0;top:568px;width:1200px;text-align:center}
.support-title{font-size:34px;line-height:44px;margin-bottom:18px}
.support-head p{font-size:12.5px;line-height:18px;margin-bottom:12px}
.card{top:730px;width:413px;height:163px;border-radius:18px;display:flex;align-items:center;gap:26px;padding:0 32px;color:var(--white);font-size:12.5px;line-height:18px}
.card.teal{left:179px;background:linear-gradient(90deg,var(--teal),var(--teal-light))}
.card.green{left:608px;background:linear-gradient(90deg,var(--green),var(--green-light))}
.card .icon{flex:none;width:92px;height:92px;border-radius:50%;background:var(--white);display:flex;align-items:center;justify-content:center}

/* postoperative */
.postop{height:600px;background:var(--muted-bg)}
.postop h2{left:90px;top:128px;font-size:34px}
.postop .copy{left:90px;top:190px;width:460px;font-size:12.5px;line-height:18px}
.postop .copy p{margin-bottom:14px}
.postop .checks{width:430px}
.postop .closing{left:110px;top:515px;width:430px;font-size:12.5px;line-height:22px;z-index:3}
.postop .circle{left:615px;top:60px;width:495px;height:495px;border-radius:50%;background:var(--white)}
.postop .robot{left:545px;top:70px;width:560px;height:570px;z-index:2;background:linear-gradient(180deg,rgba(215,220,224,.9),rgba(188,196,204,.85) 60%,rgba(140,170,210,.8) 78%,rgba(170,170,170,.85));border-radius:30px}

/* commitment */
.commitment{height:610px}
.commitment h2{left:0;top:130px;width:1200px;text-align:center;font-size:34px}
.commitment p{left:220px;top:190px;width:760px;text-align:center;font-size:12.5px;line-height:18px}
.commitment .photo{left:258px;top:284px;width:684px;height:381px;border-radius:28px;z-index:3;background:linear-gradient(120deg,#cbb89c 0%,#a7b9c8 45%,#6e9fc7 70%,#6b7f59 100%)}

/* footer */
.footer{height:470px;background:var(--footer);color:var(--white)}
.footer .brand{left:0;top:160px;width:1200px;text-align:center;font-size:44px;color:var(--white)}
.footer ul{list-style:none;left:0;top:236px;width:1200px;display:flex;justify-content:center;gap:26px;font-size:12px;text-transform:uppercase}
.socials{left:0;top:280px;width:1200px;display:flex;justify-content:center;gap:8px}
.socials span{width:44px;height:44px;border-radius:50%;background:#3a3a3a}
.footer .rule{left:88px;top:396px;width:1024px;height:1px;background:#444}
.footer .copyright{left:88px;top:424px;font-size:12px}
.footer .legal{right:88px;top:424px;display:flex;gap:30px;font-size:11px}
.to-top{left:1132px;top:383px;width:40px;height:40px;border-radius:50%;background:var(--green);display:flex;align-items:center;justify-content:center}
</style>
</head>
<body>

<section class="hero">
  <div class="abs hero-photo" role="img" aria-label="Doctor operating an imaging scanner while a patient lies inside"></div>
  <nav class="abs nav">
    <span class="brand">Dr. Mateus Vilhena</span>
    <ul><li>About me</li><li>Approach</li><li>3D Technology</li><li>Support</li><li>Postoperative care</li><li>Commitment</li></ul>
    <span class="lang">ENG ▾</span>
  </nav>
  <h1 class="abs">Caring with <span class="accent">Precision,</span> Treating with Empathy</h1>
  <p class="abs">Robotic surgery represents one of the most relevant advances in modern medicine. It offers more accuracy, less bleeding and faster recovery. But, above technology, there is the commitment to the best decision for each patient.</p>
  <div class="abs dots"><span></span><span></span><span></span></div>
</section>

<section class="intro">
  <div class="abs intro-text">
    <p>Here, we understand that not every case needs surgery, and much less that every surgery needs to be robotic. We work based on the best scientific evidence, international guidelines and, when necessary, with the support of artificial intelligence technologies to help define the most appropriate conduct.</p>
    <p>Each patient is unique. Therefore, before any decision, we seek to understand in depth the disease, the exams and, above all, the expectations and priorities of those who come to us. This attentive listening is the first step towards a safe and shared choice.</p>
    <p>When surgery is the best route, we use custom 3D models based on the patient's own exams to plan the procedure with maximum accuracy. This approach has already demonstrated a direct impact on better outcomes, with less surgical time, less bleeding, and more safety.</p>
    <p>But our care goes beyond the operating room. We know that a good outcome also depends on how the patient gets to the hospital and how he returns home. <b>That's why we offer:</b></p>
  </div>
  <div class="abs offer-box">
    <div class="offer"><span class="num">1.</span><span>An administrative team that takes care of all contact with hospitals and health plans, avoiding wear and tear with bureaucracies.</span></div>
    <div class="offer"><span class="num">2.</span><span>A group of nurses and physiotherapists who monitor the postoperative period with visits and guidance at home.</span></div>
    <div class="offer"><span class="num">3.</span><span>A direct contact channel to clarify doubts and ensure peace of mind throughout the process.</span></div>
  </div>
  <p class="abs goal">Our goal is for each patient to <b>feel safe, well-guided, and truly cared for.</b> Because we believe<br>that the best medicine is the one that unites knowledge, technology and humanity.</p>
  <div class="abs divider"></div>
</section>

<section class="about">
  <div class="abs back-square"></div>
  <div class="abs frame"></div>
  <div class="abs photo" role="img" aria-label="Portrait of the urologist in blue scrubs with a stethoscope, arms crossed"></div>
  <h2 class="abs"><span class="accent">About</span> Dr. Mateus Vilhena</h2>
  <div class="abs copy">
    <p>Caring with precision, treating with empathy! I am a urologist with a focus on robotic surgery and comprehensive patient care. More than a technique, I believe that good medicine begins with listening, careful planning, and commitment to what is best for each person.</p>
    <p>My mission is to offer treatments based on science, technology, and humanity — respecting each patient's time, choices, &amp; goals.</p>
  </div>
</section>

<section class="approach">
  <div class="abs circle"></div>
  <div class="abs robot" role="img" aria-label="Robotic surgical arms with fine instruments"></div>
  <h2 class="abs"><span class="accent">Our</span> Approach</h2>
  <div class="abs copy">
    <p>Not every treatment needs to be surgical. Not every surgery needs to be robotic.</p>
    <p>Robotic surgery is a great advance, but it must be indicated with criteria. Before proposing any intervention, we evaluate the case broadly:</p>
    <ul class="checks">
      <li><svg width="14" height="14" viewBox="0 0 14 14"><circle cx="7" cy="7" r="7" fill="#8cc63f"/><path d="M4 7.2l2 2 4-4" stroke="#fff" stroke-width="1.6" fill="none"/></svg>We use the most up-to-date medical guidelines;</li>
      <li><svg width="14" height="14" viewBox="0 0 14 14"><circle cx="7" cy="7" r="7" fill="#8cc63f"/><path d="M4 7.2l2 2 4-4" stroke="#fff" stroke-width="1.6" fill="none"/></svg>We make use of artificial intelligence tools to support clinical decision-making;</li>
      <li><svg width="14" height="14" viewBox="0 0 14 14"><circle cx="7" cy="7" r="7" fill="#8cc63f"/><path d="M4 7.2l2 2 4-4" stroke="#fff" stroke-width="1.6" fill="none"/></svg>We conduct frank conversations about the real needs, benefits and risks of each approach.</li>
    </ul>
  </div>
  <p class="abs focus">Our focus is to ensure that the <b>patient is referred to the option</b> with the greatest potential for<br>outcome — be it surgical, clinical, or even active surveillance.</p>
</section>

<section class="planning">
  <div class="abs frame"></div>
  <div class="abs media" role="img" aria-label="3D anatomical reconstruction of kidneys, vessels and skeleton"></div>
  <div class="abs play"><svg width="22" height="24" viewBox="0 0 22 24"><path d="M4 3l15 9-15 9z" fill="#fff"/></svg></div>
  <h2 class="abs planning-title"><span class="accent">Planning</span> with 3D Technology</h2>
  <p class="abs copy">In kidney and prostate surgeries, we adopt the use of personalized 3D models, created from the patient's own exams. These models help to understand the anatomy precisely, making it easier to choose the best surgical approach. We have already demonstrated that this planning reduces bleeding, surgical time, and even changes the strategy in almost half of the cases evaluated.</p>
  <div class="abs support-head">
    <h2 class="support-title"><span class="accent">Pre</span>-Procedure Support</h2>
    <p>Your focus should be on your health, not bureaucracy.</p>
    <p>We know that the moment before a procedure can be surrounded by doubts and<br>anxiety. That's why we offer:</p>
  </div>
  <div class="abs card teal">
    <span class="icon"><svg width="48" height="48" viewBox="0 0 48 48" fill="none" stroke="#2f7192" stroke-width="2"><rect x="12" y="6" width="24" height="32" rx="2"/><path d="M17 14h14M17 20h14M17 26h8"/><circle cx="24" cy="38" r="6" fill="#fff"/><path d="M21 38l2 2 4-4"/></svg></span>
    <span>An office dedicated to solving all the bureaucratic part with hospitals and health plans;</span>
  </div>
  <div class="abs card green">
    <span class="icon"><svg width="48" height="48" viewBox="0 0 48 48" fill="none" stroke="#2f7192" stroke-width="2"><circle cx="17" cy="14" r="5"/><circle cx="31" cy="14" r="5"/><path d="M8 36v-8a9 9 0 0 1 18 0v8M22 36v-8a9 9 0 0 1 18 0v8"/><path d="M20 40c2-3 6-3 8 0"/></svg></span>
    <span>Close, agile and human support, so that you can focus on what really matters: your preparation and well-being.</span>
  </div>
</section>

<section class="postop">
  <div class="abs circle"></div>
  <div class="abs robot" role="img" aria-label="Robotic surgical system with arms over an operating table"></div>
  <h2 class="abs"><span class="accent">Postoperative</span> Care</h2>
  <div class="abs copy">
    <p>Your focus should be on your health, not bureaucracy.</p>
    <p>We know that the moment before a procedure can be surrounded by doubts and anxiety. That's why we offer:</p>
    <ul class="checks">
      <li><svg width="14" height="14" viewBox="0 0 14 14"><circle cx="7" cy="7" r="7" fill="#8cc63f"/><path d="M4 7.2l2 2 4-4" stroke="#fff" stroke-width="1.6" fill="none"/></svg>Home visits when necessary;</li>
      <li><svg width="14" height="14" viewBox="0 0 14 14"><circle cx="7" cy="7" r="7" fill="#8cc63f"/><path d="M4 7.2l2 2 4-4" stroke="#fff" stroke-width="1.6" fill="none"/></svg>Practical guidance on movement, feeding and medications;</li>
      <li><svg width="14" height="14" viewBox="0 0 14 14"><circle cx="7" cy="7" r="7" fill="#8cc63f"/><path d="M4 7.2l2 2 4-4" stroke="#fff" stroke-width="1.6" fill="none"/></svg>Monitoring of signs that deserve attention — always with an attentive clinical eye.</li>
    </ul>
  </div>
  <p class="abs closing">In addition, <b>we maintain a direct contact channel</b> to clarify doubts,<br>adapt conducts and support your recovery.</p>
</section>

<section class="commitment">
  <h2 class="abs"><span class="accent">Commitment</span> to the Patient</h2>
  <p class="abs">We believe that the best result comes from the sum of knowledge, technology and empathy. Our commitment is to deeply understand what you are facing, clearly present all available options and build, together, the best path for your treatment. Because each patient is unique — and deserves to be cared for as such.</p>
  <div class="abs photo" role="img" aria-label="Doctor in scrubs smiling and talking with an older patient"></div>
</section>

<footer class="footer" style="position:relative">
  <div class="abs brand">Dr. Mateus Vilhena</div>
  <ul class="abs"><li>Home</li><li>About me</li><li>Approach</li><li>3D Technology</li><li>Support</li><li>Postoperative care</li><li>Commitment</li></ul>
  <div class="abs socials"><span aria-label="Social profile"></span><span aria-label="Social profile"></span><span aria-label="Social profile"></span><span aria-label="Social profile"></span></div>
  <div class="abs to-top"><svg width="14" height="10" viewBox="0 0 14 10"><path d="M2 8l5-5 5 5" stroke="#fff" stroke-width="2" fill="none"/></svg></div>
  <div class="abs rule"></div>
  <div class="abs copyright">Copyright © 2025- All Rights Reserved</div>
  <div class="abs legal"><span>Privacy Policy</span><span>Terms Of Services</span><span>Disclaimer</span></div>
</footer>

</body>
</html>
```